Business Card Professional Clean - Lumavault

Create a business card for my company that deals with Cryptocurrencies. I have a few designs ideas that I'd like to be implemented. Thanks! I will include the logo files, and a link to the design styles that I like.

Target Market(s)

Professionals

Industry/Entity Type

Consulting

Contact Information for Business Card

Name: Mark Dunn
Title: CEO/Technical Director
Phone: (587)943-0586
E-mail: mdunn@lumavault.ca
Address: Suite 512, 208-3370 Harwood Avenue NW

Twitter: @LumaVaultHQ
Instagram: lumavaulthq

Colors
92b5d7
3276b5
33a6d7
85acd3
85cae6
0592cd

Requirements
Must have
• Some colors that match with the logo and the pictures I put in below.
• Ideally the finished product would look something like the attachments showing the color gradient I want.
Nice to have
• Please see some of the attachments I've included. This is very close to the final product that I would like to see. If someone could recreate something like those I would definitely feel pretty good about it.
• For the instagram and twitter please use the symbols/icon to represent it on the card.
Should not have
• No crazy colors and unprofessional styles. I just want clear info. Don't go outside the boundaries of the colors in the attachment and we should be good. No crazy weird fonts either.

```html
<!DOCTYPE html>
<html lang="en">
<head>
<meta charset="utf-8">
<title>Lumavault Business Card</title>
<link rel="stylesheet" href="https://fonts.googleapis.com/css2?family=Open+Sans:wght@300;400;600;700&display=swap">
<style>
  :root {
    --canvas: #e9ebee;
    --paper: #fbfbfb;
    --brand-blue: #0552a0;
    --accent-blue: #3276b5;
    --ink-dark: #2b2b2b;
    --ink-grey: #6b6f75;
    --rule-grey: #c4c7cc;
    --white: #ffffff;
  }
  * { box-sizing: border-box; margin: 0; padding: 0; }
  html, body {
    width: 1200px;
    height: 950px;
    overflow: hidden;
    background: var(--canvas);
    font-family: "Open Sans", Arial, sans-serif;
  }
  .sheet {
    position: relative;
    width: 1200px;
    height: 950px;
  }
  .card {
    position: absolute;
    left: 250px;
    width: 700px;
    height: 400px;
    overflow: hidden;
    box-shadow: 0 6px 18px rgba(0,0,0,0.15);
  }
  .card-front { top: 50px; background: var(--paper); }
  .card-back  { top: 490px; background: var(--brand-blue); }

  /* front: brand block */
  .brand {
    position: absolute;
    left: 40px;
    top: 150px;
    width: 250px;
    display: flex;
    flex-direction: column;
    align-items: center;
    gap: 18px;
  }
  .brand-square {
    width: 34px;
    height: 34px;
    background: var(--accent-blue);
  }
  .brand-name {
    font-weight: 300;
    font-size: 34px;
    letter-spacing: 4px;
    text-transform: uppercase;
    color: var(--accent-blue);
  }
  .divider {
    position: absolute;
    left: 300px;
    top: 40px;
  }

  /* front: contact block */
  .contact {
    position: absolute;
    left: 370px;
    top: 56px;
  }
  .person-name {
    font-weight: 700;
    font-size: 24px;
    color: var(--brand-blue);
    letter-spacing: 0.5px;
    text-transform: uppercase;
  }
  .person-title {
    font-weight: 700;
    font-size: 16px;
    color: var(--ink-dark);
    text-transform: uppercase;
    margin-top: 2px;
  }
  .address {
    font-size: 14px;
    color: var(--ink-grey);
    line-height: 1.45;
    margin-top: 10px;
  }
  .contact-list {
    list-style: none;
    margin-top: 6px;
  }
  .contact-list li {
    display: flex;
    align-items: center;
    gap: 9px;
    font-size: 14px;
    line-height: 1.55;
    color: var(--ink-grey);
  }
  .contact-icon {
    width: 14px;
    height: 14px;
    flex: none;
  }
  .contact-dot {
    width: 12px;
    height: 12px;
    margin: 0 1px;
    border-radius: 50%;
    background: var(--accent-blue);
    flex: none;
  }

  /* front: web band */
  .web-band {
    position: absolute;
    right: 0;
    bottom: 0;
    width: 330px;
    height: 44px;
    background: var(--brand-blue);
    clip-path: polygon(22px 0, 100% 0, 100% 100%, 0 100%);
    display: flex;
    align-items: center;
    justify-content: center;
    color: var(--white);
    font-size: 15px;
    font-weight: 600;
    letter-spacing: 4px;
  }

  /* back */
  .back-brand {
    position: absolute;
    inset: 0;
    display: flex;
    align-items: center;
    justify-content: center;
    color: var(--white);
    font-weight: 300;
    font-size: 56px;
    letter-spacing: 6px;
    text-transform: uppercase;
  }
</style>
</head>
<body>
<main class="sheet">
  <section class="card card-front">
    <div class="brand">
      <span class="brand-square"></span>
      <span class="brand-name">Lumavault</span>
    </div>

    <svg class="divider" width="40" height="320" viewBox="0 0 40 320" aria-hidden="true">
      <line x1="34" y1="0" x2="6" y2="320" stroke="var(--rule-grey)" stroke-width="1.5"/>
    </svg>

    <div class="contact">
      <p class="person-name">Mark Dunn</p>
      <p class="person-title">CEO/Technical Director</p>
      <p class="address">Suite 512, 208-3370<br>Harwood Avenue NW</p>
      <ul class="contact-list">
        <li>
          <svg class="contact-icon" viewBox="0 0 16 16" aria-hidden="true">
            <path d="M4 1.5 L6.5 5 L5 6.5 C6 8.5 7.5 10 9.5 11 L11 9.5 L14.5 12 L13 14.5 C7 14 2 9 1.5 3 Z" fill="var(--accent-blue)"/>
          </svg>
          <span>(587)943-0586</span>
        </li>
        <li>
          <svg class="contact-icon" viewBox="0 0 16 16" aria-hidden="true">
            <rect x="1" y="3" width="14" height="10" rx="1" fill="var(--accent-blue)"/>
            <polyline points="1.5,3.5 8,9 14.5,3.5" fill="none" stroke="var(--white)" stroke-width="1.3"/>
          </svg>
          <span>mdunn@lumavault.ca</span>
        </li>
        <li>
          <span class="contact-dot"></span>
          <span>@LumaVaultHQ</span>
        </li>
        <li>
          <span class="contact-dot"></span>
          <span>lumavaulthq</span>
        </li>
      </ul>
    </div>

    <div class="web-band">www.lumavault.ca</div>
  </section>

  <section class="card card-back">
    <div class="back-brand">Lumavault</div>
  </section>
</main>
</body>
</html>
```